BrookvaleLogic Website Design

To design a website for BrookvaleLogic, a software development company. The website should reflect the branding of our company, which is Smart, Beautiful, and Sophisticated. The existing website is www.brookvalelogic-example.com.sg

```html
<!DOCTYPE html>
<html lang="en">
<head>
<meta charset="utf-8">
<title>BrookvaleLogic — Software Development</title>
<link href="https://fonts.googleapis.com/css2?family=Lato:ital,wght@0,300;0,400;0,700;0,900;1,400&display=swap" rel="stylesheet">
<style>
:root{
  --navy:#1f3b5e;
  --navy-dark:#16304f;
  --orange:#f26522;
  --slate:#2f3b4b;
  --ink:#333;
  --light:#efefef;
  --footer:#2b2b2b;
  --footer-dark:#1e1e1e;
  --blue-link:#3b8fd1;
  --white:#fff;
}
*{box-sizing:border-box;margin:0;padding:0}
html,body{width:1200px;height:3326px;overflow:hidden}
body{font-family:'Lato',sans-serif;color:var(--ink);background:var(--white);position:relative}
section,header,footer,nav{position:absolute;left:0;width:1200px}
.abs{position:absolute}

/* header */
.site-header{top:0;height:83px;background:linear-gradient(#fff,#f1f1f1)}
.brand{left:160px;top:22px;display:flex;align-items:center;gap:10px}
.brand-mark{width:36px;height:36px;border-radius:50%;background:var(--navy)}
.brand-name{font-size:28px;font-weight:700;color:var(--navy)}
.contact{top:22px;display:flex;gap:10px;align-items:center;font-size:14px;color:#555;line-height:1.25}
.contact .ic{width:36px;height:36px;border-radius:50%;background:var(--navy);display:flex;align-items:center;justify-content:center}
.contact b{color:var(--navy);font-weight:700}

.main-nav{top:83px;height:34px;background:var(--navy-dark);display:flex;align-items:center}
.main-nav ul{list-style:none;display:flex;margin-left:160px}
.main-nav li{color:#fff;font-size:14px;font-weight:700;padding:0 26px}
.chat{position:absolute;right:160px;color:#fff;font-size:14px;font-weight:700;display:flex;gap:8px;align-items:center}

/* hero */
.hero{top:117px;height:465px;background:linear-gradient(100deg,#4a4238 0%,#7b6f60 35%,#5d5a55 60%,#3a3f46 100%)}
.hero-copy{left:160px;top:130px;color:#fff}
.hero-copy h1{font-weight:300;font-size:33px;line-height:1.05}
.hero-copy h1 strong{display:block;font-weight:700;font-size:36px}
.hero-copy p{width:360px;font-size:13px;margin-top:12px;line-height:1.4;opacity:.9}
.btn{display:inline-block;font-size:14px;font-weight:700;padding:9px 16px;border-radius:2px;color:#fff;background:var(--orange)}
.btn-outline{background:transparent;border:1px solid #fff}
.monitor{left:568px;top:62px;width:472px;height:345px}
.monitor-frame{width:472px;height:300px;background:#111;border-radius:8px;padding:14px}
.monitor-screen{width:100%;height:100%;background:linear-gradient(135deg,#2b2b2b,#7a2222 55%,#d9d9d9)}
.monitor-stand{margin:0 auto;width:110px;height:38px;background:linear-gradient(#ccc,#999)}
.monitor-base{margin:0 auto;width:200px;height:7px;background:#888;border-radius:3px}
.hero-strip{position:absolute;left:0;top:404px;width:1200px;height:61px;background:rgba(0,0,0,.45);color:#fff;font-size:15px;padding:22px 0 0 160px}

/* clients */
.clients{top:582px;height:83px;background:var(--light);display:flex;align-items:center}
.clients-lead{margin-left:180px;font-size:13px;color:#666;line-height:1.2;width:130px}
.client{font-size:22px;font-weight:700;color:#777;margin-left:60px;letter-spacing:1px}

/* welcome */
.welcome{top:665px;height:429px;text-align:center}
.welcome h2{margin-top:40px;font-size:30px;font-weight:300;color:#444}
.welcome h2 span{color:var(--blue-link)}
.welcome .lead{width:560px;margin:10px auto 0;font-size:12px;color:#999;line-height:1.4}
.services{display:flex;justify-content:center;gap:20px;margin-top:34px}
.service{width:220px}
.service .circle{width:96px;height:96px;border-radius:50%;background:var(--navy);margin:0 auto;display:flex;align-items:center;justify-content:center;border:4px solid #dde3ea}
.service.active .circle{background:var(--orange);border-color:#f9d2bd}
.service h3{font-size:15px;font-weight:700;margin-top:16px;color:var(--navy)}
.service.active h3{color:var(--orange)}
.service p{font-size:12px;color:#999;line-height:1.35;margin-top:6px}

/* discover */
.discover{top:1094px;height:457px;background:var(--slate);color:#fff}
.discover h2{text-align:center;margin-top:28px;font-size:27px;font-weight:300}
.discover .lead{text-align:center;width:560px;margin:6px auto 0;font-size:12px;color:#aab;line-height:1.4}
.laptop{left:166px;top:150px;width:400px;height:212px}
.laptop-lid{margin:0 auto;width:320px;height:190px;background:#ccc;border-radius:8px 8px 0 0;padding:10px}
.laptop-screen{width:100%;height:100%;background:linear-gradient(135deg,#c7d6dd,#3d5b6d 60%,#9aa8ae)}
.laptop-base{width:400px;height:14px;background:linear-gradient(#ddd,#999);border-radius:0 0 14px 14px}
.about{left:588px;top:160px;width:455px}
.about h3{font-size:19px;font-weight:400}
.about .bold{font-size:13px;font-weight:700;margin-top:14px;line-height:1.4}
.about .body{font-size:11px;color:#aab;margin-top:12px;line-height:1.5}
.about .actions{margin-top:26px;display:flex;gap:12px}

/* works */
.works{top:1551px;height:928px;text-align:center}
.works h2{margin-top:60px;font-size:30px;font-weight:300;color:#444}
.filters{display:flex;justify-content:center;margin-top:14px;font-size:13px;color:#555}
.filters span{padding:3px 10px;border-right:1px solid #ccc}
.filters span:last-child{border:0}
.filters .on{background:var(--orange);color:#fff;border:0}
.grid{left:152px;top:172px;width:888px;height:710px}
.tile{position:absolute}
.overlay{background:#4a78a5;display:flex;flex-direction:column;align-items:center;justify-content:center;color:#fff}
.overlay .small{font-size:14px}
.overlay .title{font-size:17px;font-weight:700;margin-top:4px}
.overlay .btns{display:flex;margin-top:14px}
.overlay .btns div{width:46px;height:46px;display:flex;align-items:center;justify-content:center}

/* testimonials */
.trusted{top:2479px;height:430px;background:var(--slate);color:#fff;text-align:center}
.trusted h2{margin-top:56px;font-size:29px;font-weight:400}
.avatars{display:flex;justify-content:center;gap:6px;margin-top:36px}
.avatars div{width:66px;height:66px;border-radius:50%;border:3px solid #fff;background:linear-gradient(#b9b4ae,#6f6a66)}
.quote{width:830px;margin:36px auto 0;font-size:13px;font-style:italic;line-height:1.6;color:#dde}
.author{margin-top:16px;font-size:13px;font-weight:700}
.role{font-size:13px;color:var(--blue-link)}
.dots{display:flex;justify-content:center;gap:6px;margin-top:20px}
.dots span{width:8px;height:8px;border-radius:50%;background:#778}
.dots .on{background:#fff}

/* help bar */
.help{top:2909px;height:83px;background:var(--footer-dark);color:#fff;display:flex;align-items:center}
.help p{margin-left:145px;font-size:18px;color:#ccc}
.help p b{color:#fff}
.help .phone{position:absolute;right:140px;font-size:28px;font-weight:700;display:flex;gap:12px;align-items:center}

/* footer */
.site-footer{top:2992px;height:291px;background:var(--footer);color:#ccc}
.col{position:absolute;top:26px;font-size:13px}
.col h4{color:#fff;font-size:15px;font-weight:700;margin-bottom:10px}
.col ul{list-style:none}
.col li{line-height:1.65;padding-left:12px;position:relative}
.col li:before{content:"•";position:absolute;left:0;color:#999}
.col li.current{color:var(--blue-link)}
.newsletter input{display:block;width:205px;height:32px;background:#3a3a3a;border:1px solid #555;color:#aaa;font:13px 'Lato',sans-serif;padding:0 8px;margin-top:10px}
.newsletter .btn{margin:8px 0 0 95px;padding:7px 22px}
.social{display:flex;gap:6px;margin-top:8px}
.social span{width:22px;height:22px;border-radius:50%;background:#777}
.copyright{position:absolute;left:0;top:3283px;width:1200px;height:43px;background:var(--footer-dark);color:#999;font-size:12px;display:flex;align-items:center;justify-content:space-between;padding:0 160px 0 145px}
.footer-links{display:flex;gap:12px}
</style>
</head>
<body>

<header class="site-header">
  <div class="brand abs"><span class="brand-mark"></span><span class="brand-name">BrookvaleLogic</span></div>
  <div class="contact abs" style="left:648px">
    <span class="ic"><svg width="18" height="18" viewBox="0 0 24 24"><path fill="#fff" d="M6.6 10.8a15 15 0 0 0 6.6 6.6l2.2-2.2c.3-.3.7-.4 1-.2 1.1.4 2.3.6 3.6.6.6 0 1 .4 1 1V20c0 .6-.4 1-1 1A17 17 0 0 1 3 4c0-.6.4-1 1-1h3.5c.6 0 1 .4 1 1 0 1.3.2 2.5.6 3.6.1.3 0 .7-.2 1z"/></svg></span>
    <div>Question?<br><b>Call 1-800-555-0142</b></div>
  </div>
  <div class="contact abs" style="left:870px">
    <span class="ic"><svg width="18" height="14" viewBox="0 0 20 14"><rect x="1" y="1" width="18" height="12" fill="none" stroke="#fff" stroke-width="2"/><path d="M1 1l9 7 9-7" fill="none" stroke="#fff" stroke-width="2"/></svg></span>
    <div>Email Us<br><b>info@brookvalelogic-example.com</b></div>
  </div>
</header>

<nav class="main-nav">
  <ul><li>Home</li><li>Services</li><li>About Us</li><li>Portfolio</li><li>Contact</li></ul>
  <div class="chat"><svg width="24" height="18" viewBox="0 0 24 18"><ellipse cx="10" cy="7" rx="10" ry="7" fill="#fff"/><ellipse cx="16" cy="11" rx="8" ry="6" fill="#fff" stroke="#16304f" stroke-width="1.5"/></svg>Chat with us now</div>
</nav>

<section class="hero" role="img" aria-label="Blurred office interior photograph behind the headline">
  <div class="hero-copy abs">
    <h1>We provide you<strong>the best solution</strong>for your business</h1>
    <p>Lorem ipsum dolor sit amet, consectetuer adipiscing elit. Aenean commodo ligula eget dolor. Aenean massa. Cum sociis natoque penatibus et magnis dis parturient montes, nasc.</p>
    <span class="btn" style="margin-top:14px">Request a quote</span>
  </div>
  <div class="monitor abs">
    <div class="monitor-frame"><div class="monitor-screen" role="img" aria-label="Website screenshot of a sports footwear store on the monitor"></div></div>
    <div class="monitor-stand"></div><div class="monitor-base"></div>
  </div>
  <div class="hero-strip">Let us handle the <b>tehnology</b>, so you can focus on your <b>business</b></div>
</section>

<section class="clients">
  <div class="clients-lead">Over <b>200</b> happy customers we'd like you to meet</div>
  <span class="client">VERADINE</span>
  <span class="client">ORLANTO</span>
  <span class="client">HAVENTA</span>
  <span class="client">QUILLMARK</span>
</section>

<section class="welcome">
  <h2>Welcome to <span>BrookvaleLogic Agency</span></h2>
  <p class="lead">Lorem ipsum dolor sit amet, consectetuer adipiscing elit. Aenean commodo ligula eget dolor. Aenean massa. Cum sociis natoque penatibus et magnis dis parturient montes, nascetur ridiculus mus. Donec quam felis, ultricies nec, pellentesque eu, pretium quis, sem.</p>
  <div class="services">
    <div class="service active">
      <div class="circle"><svg width="40" height="40" viewBox="0 0 40 40" fill="none" stroke="#fff" stroke-width="2.5"><circle cx="20" cy="20" r="14"/><path d="M20 10v10l7 5"/></svg></div>
      <h3>Strategy &amp; Consulting</h3>
      <p>Online Business Consulting<br>Website Planning<br>Online Marketing Strategy</p>
    </div>
    <div class="service">
      <div class="circle"><svg width="40" height="40" viewBox="0 0 40 40" fill="none" stroke="#fff" stroke-width="2.5"><rect x="6" y="6" width="28" height="28" rx="3"/><path d="M11 27l7-8 5 5 7-10"/></svg></div>
      <h3>Online Marketing</h3>
      <p>Search Engine Optimization<br>PPC Marketing<br>Conversion Rate Optimization</p>
    </div>
    <div class="service">
      <div class="circle"><svg width="40" height="40" viewBox="0 0 40 40" fill="none" stroke="#fff" stroke-width="3"><path d="M10 30L30 10M10 10l20 20"/></svg></div>
      <h3>Design &amp; Development</h3>
      <p>Logos &amp; Branding<br>Website Development<br>Ecommerce Websites</p>
    </div>
    <div class="service">
      <div class="circle"><svg width="40" height="40" viewBox="0 0 40 40" fill="none" stroke="#fff" stroke-width="2.5"><rect x="12" y="5" width="16" height="30" rx="3"/><circle cx="20" cy="30" r="1.5" fill="#fff"/></svg></div>
      <h3>Mobile Development</h3>
      <p>Mobile App Development<br>Responsive Website Design<br>Mobile Website Design</p>
    </div>
  </div>
</section>

<section class="discover">
  <h2>Discover more about our solutions</h2>
  <p class="lead">Lorem ipsum dolor sit amet, consectetuer adipiscing elit. Aenean commodo ligula eget dolor. Aenean massa. Cum sociis natoque penatibus et magnis dis parturient montes.</p>
  <div class="laptop abs">
    <div class="laptop-lid"><div class="laptop-screen" role="img" aria-label="Laptop screen showing a photography website"></div></div>
    <div class="laptop-base"></div>
  </div>
  <div class="about abs">
    <h3>We are a group of IT specialists lorem ipsum dolor</h3>
    <p class="bold">Lorem ipsum dolor sit amet, consectetuer adipiscing elit. Aenean commodo ligula eget dolor. Aenean massa. Cum sociis natoque penatibus et magnis dis parturient montes, nasc.</p>
    <p class="body">Nam pretium turpis et arcu. Duis arcu tortor, suscipit eget, imperdiet nec, imperdiet iaculis, ipsum. Sed aliquam ultrices mauris. Integer ante arcu, accumsan a, consectetuer eget, posuere ut, mauris. Praesent adipiscing. Phasellus ullamcorper ipsum rutrum nunc. Nunc nonummy metus. Vestibulum volutpat pretium libero. Cras id dui. Aenean ut eros et nisl sagittis vestibulum. Nullam nulla eros, ultricies sit amet, nonummy id, imperdiet feugiat, pede. Sed lectus.</p>
    <div class="actions"><span class="btn btn-outline">Learn More</span><span class="btn">Request a quote</span></div>
  </div>
</section>

<section class="works">
  <h2>Featured works</h2>
  <div class="filters"><span class="on">All</span><span>APP</span><span>Ecommerce</span><span>Charity</span><span>Events</span></div>
  <div class="grid abs">
    <div class="tile" style="left:0;top:0;width:294px;height:355px;background:linear-gradient(#1b3a2a,#0e1a14)" role="img" aria-label="Athlete campaign website artwork"></div>
    <div class="tile" style="left:0;top:355px;width:294px;height:355px;background:linear-gradient(#222,#7a5e1a 50%,#111)" role="img" aria-label="Gold sports shoe product page"></div>
    <div class="tile" style="left:297px;top:0;width:294px;height:216px;background:linear-gradient(#0d0f1a,#2a3040)" role="img" aria-label="Dark sports event website"></div>
    <div class="tile overlay" style="left:297px;top:216px;width:294px;height:306px">
      <div class="small">Photography</div>
      <div class="title">LOGO, PRINTS, WEB DESIGN</div>
      <div class="btns">
        <div style="background:var(--orange)"><svg width="20" height="20" viewBox="0 0 20 20" fill="none" stroke="#fff" stroke-width="2.5"><circle cx="8" cy="8" r="6"/><path d="M12.5 12.5L18 18"/></svg></div>
        <div style="background:#fff"><svg width="20" height="20" viewBox="0 0 20 20" fill="none" stroke="#666" stroke-width="2.5"><path d="M8 12l4-4M6 10l-2 2a3 3 0 0 0 4 4l2-2M14 10l2-2a3 3 0 0 0-4-4l-2 2"/></svg></div>
      </div>
    </div>
    <div class="tile" style="left:297px;top:522px;width:294px;height:188px;background:linear-gradient(#1a1d24,#5a6068)" role="img" aria-label="Watch product website"></div>
    <div class="tile" style="left:594px;top:0;width:294px;height:258px;background:linear-gradient(#f2f2f2,#c9c9c9)" role="img" aria-label="Footwear store homepage"></div>
    <div class="tile" style="left:594px;top:258px;width:294px;height:208px;background:linear-gradient(#fff,#e8c9b8)" role="img" aria-label="Fashion retail website"></div>
    <div class="tile" style="left:594px;top:466px;width:294px;height:244px;background:linear-gradient(#b7e35a,#3f9f2f)" role="img" aria-label="Fresh drinks product website"></div>
  </div>
</section>

<section class="trusted">
  <h2>Trusted by more than thousand clinets lorem ipsum</h2>
  <div class="avatars" role="img" aria-label="Client portrait photos">
    <div></div><div></div><div></div><div></div><div></div>
  </div>
  <p class="quote">Lorem ipsum dolor sit amet, consectetuer adipiscing elit. Aenean commodo ligula eget dolor. Aenean massa. Cum sociis natoque penatibus et magnis dis parturient montes, nascetur ridiculus mus. Donec quam felis, ultricies nec, pellentesque eu, pretium quis, sem. Nulla consequat massa quis enim. Donec pede justo, fringilla vel, aliquet nec, vulputate eget, arcu. In enim justo</p>
  <div class="author">Marin Keller</div>
  <div class="role">Designer Northfield Studio</div>
  <div class="dots"><span class="on"></span><span></span><span></span><span></span><span></span></div>
</section>

<section class="help">
  <p><b>Need Help?</b> Call Us, Monday to Friday, 10 AM to 6PM</p>
  <div class="phone"><svg width="26" height="26" viewBox="0 0 24 24"><path fill="#fff" d="M6.6 10.8a15 15 0 0 0 6.6 6.6l2.2-2.2c.3-.3.7-.4 1-.2 1.1.4 2.3.6 3.6.6.6 0 1 .4 1 1V20c0 .6-.4 1-1 1A17 17 0 0 1 3 4c0-.6.4-1 1-1h3.5c.6 0 1 .4 1 1 0 1.3.2 2.5.6 3.6.1.3 0 .7-.2 1z"/></svg>01.55.01.20.30</div>
</section>

<footer class="site-footer">
  <div class="col" style="left:148px">
    <h4>Services</h4>
    <ul><li>Online Stores</li><li>Social Media</li><li>Online Marketing</li><li class="current">Digital Strategy</li><li>Responsive / Mobile Designs</li><li>Hosting &amp; Domain Registration</li></ul>
  </div>
  <div class="col" style="left:380px">
    <h4>Online Marketing</h4>
    <ul><li>Email Marketing</li><li>Search Engine Optimisation</li><li>Paid Search Management</li></ul>
    <h4 style="margin-top:14px">Web Development</h4>
    <ul><li>Web Design</li><li>Content Management Systems</li><li>Web Application Development</li></ul>
  </div>
  <div class="col" style="left:618px">
    <h4>About Us</h4>
    <ul><li>Our Team</li><li>Careers</li><li>Affiliate</li><li>News</li><li>Blog</li><li>Testimonials</li></ul>
  </div>
  <div class="col newsletter" style="left:830px">
    <h4>Newsletter Signup</h4>
    <p style="width:210px;line-height:1.3">Signup for our daily email by entering your information below</p>
    <input type="text" value="email address" aria-label="Email address">
    <span class="btn">SUBMIT</span>
    <h4 style="margin-top:14px;margin-bottom:0">Stay Connected</h4>
    <div class="social"><span></span><span></span><span></span><span></span><span></span></div>
  </div>
</footer>

<div class="copyright">
  <span>Copyright © 2014</span>
  <div class="footer-links"><span>Home</span><span>Services</span><span>Portfolio</span><span>About Us</span><span>Blog</span><span>Contact</span></div>
</div>

</body>
</html>
```